Stonevale Business Card Design

The Stonevale Co is an aggregate (crushing) equipment dealer serving Western Canadian provinces. Stonevale is a distributor of aggregate equipment for different manufacturers.

We are looking to change and update the existing business card which has been used since the existence of the company. A copy of existing card has been attached for reference. The Stonevale Co logo we want to remain the same and we want the green color to remain the same.

We are wanting something new with a different look. A refreshing card to show a new modern and updated look. No longer wanting to have the manufacturers on the back of the card but something more like our logo on the back of the card with a statement like "Crushing Solutions"

ideas could be:
- card can be different colors on front and back
- front or reverse of the card could possibly be the green color with the logo in black

Target Market(s)

Owners of Aggregate/Crushing companies

Contact Information for Business Card

see above

Requirements
Must have
• - logo to remain same along with same font within logo
• - green color to remain same
Nice to have
• as noted above under project description
Should not have

```html
<!DOCTYPE html>
<html lang="en">
<head>
<meta charset="utf-8">
<title>Stonevale Business Card</title>
<link rel="stylesheet" href="https://fonts.googleapis.com/css2?family=Jost:wght@500;600;700&family=Anton&display=swap">
<style>
  :root {
    --stage: #c3c3c3;
    --paper: #ffffff;
    --ink: #111111;
    --olive: #8f8a17;
    --band: #000000;
    --on-olive: #ffffff;
  }
  * { margin: 0; padding: 0; box-sizing: border-box; }
  html, body { width: 1200px; height: 1000px; overflow: hidden; }
  body { background: var(--stage); position: relative; font-family: "Jost", sans-serif; }

  .card { position: absolute; width: 722px; height: 414px; overflow: hidden; }
  .card-front { left: 237px; top: 76px; background: var(--paper); }
  .card-back { left: 238px; top: 510px; background: var(--olive); }

  .identity { position: absolute; left: 0; top: 146px; width: 602px; text-align: center; }
  .person-name {
    font-weight: 700; font-size: 52px; line-height: 56px; letter-spacing: 1px; color: var(--ink);
  }
  .name-rule { width: 378px; height: 3px; background: var(--olive); margin: 4px auto 0 auto; }
  .email { font-weight: 600; font-size: 21px; line-height: 26px; margin-top: 4px; color: var(--ink); }
  .direct { font-weight: 600; font-size: 15px; line-height: 20px; color: var(--ink); }

  .services {
    position: absolute; left: 61px; top: 350px; display: flex; align-items: center;
    font-family: "Anton", sans-serif; font-size: 27px; letter-spacing: 2px; color: var(--ink);
  }
  .service-divider { width: 3px; height: 40px; background: var(--olive); margin: 0 16px; }

  .address {
    position: absolute; left: 436px; top: 196px; width: 360px; height: 22px;
    transform: rotate(-90deg); text-align: center;
    font-family: "Anton", sans-serif; font-size: 14px; letter-spacing: 1.6px; line-height: 22px;
    color: var(--olive); white-space: nowrap;
  }
  .company-band { position: absolute; left: 631px; top: 0; width: 91px; height: 414px; background: var(--band); }
  .company-name {
    position: absolute; left: 493px; top: 187px; width: 370px; height: 40px;
    transform: rotate(-90deg); text-align: center;
    font-family: "Anton", sans-serif; font-size: 30px; line-height: 40px; letter-spacing: 2.5px;
    color: var(--on-olive); white-space: nowrap;
  }

  .brand-lockup {
    position: absolute; left: 0; top: 180px; width: 722px;
    display: flex; justify-content: center; align-items: center; gap: 16px;
  }
  .brand-dot { width: 34px; height: 34px; border-radius: 50%; background: var(--on-olive); }
  .brand-name { font-weight: 600; font-size: 40px; color: var(--on-olive); letter-spacing: 1px; }

  .contact-line {
    position: absolute; left: 0; top: 354px; width: 722px; text-align: center;
    font-weight: 600; font-size: 16px; line-height: 21px; color: var(--on-olive);
  }
</style>
</head>
<body>
  <section class="card card-front">
    <div class="identity">
      <h1 class="person-name">DALE MORROW</h1>
      <div class="name-rule"></div>
      <p class="email">dale@stonevale.ca</p>
      <p class="direct">Direct: 780.555.0148</p>
    </div>
    <div class="services">
      <span>SCREENERS</span><span class="service-divider"></span>
      <span>CRUSHERS</span><span class="service-divider"></span>
      <span>STACKERS</span>
    </div>
    <p class="address">2210 - 48B AVENUE, RIDGEFORD, ALBERTA T0X 1A0</p>
    <div class="company-band"></div>
    <p class="company-name">THE STONEVALE CO.</p>
  </section>

  <section class="card card-back">
    <div class="brand-lockup">
      <span class="brand-dot"></span>
      <span class="brand-name">The Stonevale Co</span>
    </div>
    <div class="contact-line">
      <p>www.STONEVALE.ca</p>
      <p>Tel.: 780.555.0192 / Fax: 780.555.0173</p>
    </div>
  </section>
</body>
</html>
```